Optometrist/Eye Care Clinic Business card with new logo attached

We are a small, independent eye care clinic in Canada. We have recently updated our logo (as attached), and would like a professional, modern and health care oriented business card to highlight our office details and our optometrist. We'd like to incorporate the blue colours as seen on our logo.

Target Market(s)

demographic: age 35-65 male/female equal

Industry/Entity Type

Health Care

Contact Information for Business Card

Name of clinic: "Amber Hollow Eye Care Optometry"

Font styles to use
Sans Serif

Colors
0355a3

Requirements
Must have
• our website: amberholloweyecare.net
• Dr Selma Okonkwo
• Optometrist
• 312-617 E Larkspur Ave
• Vancouver BC V7R 3P8
• P: 604-555-0193
• E: info@amberholloweyecare.net
Nice to have
• front side: logo/name of clinic as seen on logo attached and website
• backside: logo on the left side, and name/title/address/phone/email

```html
<!DOCTYPE html>
<html lang="en">
<head>
<meta charset="utf-8">
<title>Amber Hollow Eye Care Optometry – Business Card</title>
<link href="https://fonts.googleapis.com/css2?family=Questrial&display=swap" rel="stylesheet">
<style>
  :root {
    --backdrop: #2e2f31;
    --card: #ffffff;
    --navy: #0c3f5e;
    --brand-blue: #0355a3;
    --teal: #2a8fb5;
    --ink: #1f2f3d;
    --rule: #5aaecf;
  }
  * { margin: 0; padding: 0; box-sizing: border-box; }
  html, body {
    width: 1200px; height: 900px; overflow: hidden;
    background: var(--backdrop);
    font-family: "Questrial", "Century Gothic", sans-serif;
  }
  .canvas {
    position: relative; width: 1200px; height: 900px;
  }
  .card {
    position: absolute; left: 320px;
    width: 560px; height: 320px;
    background: var(--card);
    border-radius: 24px;
  }
  .card--front { top: 100px; }
  .card--back { top: 480px; }

  /* Front */
  .front-identity {
    position: absolute; inset: 0;
    display: flex; flex-direction: column;
    align-items: center; justify-content: center;
    text-align: center;
  }
  .clinic-name {
    color: var(--navy);
    font-weight: 400;
    text-transform: uppercase;
    line-height: 1.05;
  }
  .clinic-name__line { display: block; }
  .clinic-name__line--place { font-size: 34px; letter-spacing: 5px; }
  .clinic-name__line--service { font-size: 52px; letter-spacing: 3px; }
  .clinic-name__line--field { font-size: 24px; letter-spacing: 12px; margin-top: 4px; }
  .website {
    margin-top: 12px;
    color: var(--navy);
    font-size: 17px; letter-spacing: 3px;
    text-transform: uppercase;
  }

  /* Back */
  .back-mark {
    position: absolute; left: 40px; top: 0; bottom: 0; width: 170px;
    display: flex; flex-direction: column; align-items: center; justify-content: center;
    gap: 12px; text-align: center;
  }
  .back-mark__dot {
    width: 26px; height: 26px; border-radius: 50%;
    background: var(--brand-blue);
  }
  .back-mark__name {
    color: var(--navy); font-size: 14px; letter-spacing: 2px;
    text-transform: uppercase; line-height: 1.35;
  }
  .divider {
    position: absolute; left: 258px; top: 70px;
    width: 1.5px; height: 180px; background: var(--rule);
  }
  .contact {
    position: absolute; left: 286px; top: 96px;
    color: var(--ink); font-size: 14px; line-height: 1.3;
  }
  .contact__name {
    color: var(--teal); font-size: 19px; text-transform: uppercase; letter-spacing: 0.5px;
  }
  .contact__title { text-transform: uppercase; font-size: 13.5px; margin-bottom: 2px; }
  .contact__label { color: var(--teal); }
  .contact__address { margin-top: 10px; }
</style>
</head>
<body>
<main class="canvas">
  <section class="card card--front" aria-label="Card front">
    <div class="front-identity">
      <h1 class="clinic-name">
        <span class="clinic-name__line clinic-name__line--place">Amber Hollow</span>
        <span class="clinic-name__line clinic-name__line--service">Eye Care</span>
        <span class="clinic-name__line clinic-name__line--field">Optometry</span>
      </h1>
      <p class="website">amberholloweyecare.net</p>
    </div>
  </section>

  <section class="card card--back" aria-label="Card back">
    <div class="back-mark">
      <span class="back-mark__dot"></span>
      <span class="back-mark__name">Amber Hollow<br>Eye Care<br>Optometry</span>
    </div>
    <div class="divider"></div>
    <div class="contact">
      <p class="contact__name">Dr Selma Okonkwo</p>
      <p class="contact__title">Optometrist</p>
      <p><span class="contact__label">P:</span> 604-555-0193</p>
      <p><span class="contact__label">E:</span> info@amberholloweyecare.net</p>
      <p class="contact__address">312-617 E Larkspur Ave<br>Vancouver, British Columbia V7R 3P8</p>
    </div>
  </section>
</main>
</body>
</html>
```